Astrological planner&diary book cover.

Book cover for print paperback. Title: "Whole Stargazer Journal & Logbook – Sign One (Sign Two, Sign Three etc) 2022: Shape your days by charting Orbital and Night angles and passages, Idle Drift, Night cycles, Sky almanac, and Reversing bodies." The book is a series of Astrological diary & planner for 2022 for each Zodiac sign (12 books in total). The design template should be the same – the only difference would be the Zodiac sign image and text.
It should be neutral to positive. There is no restriction regarding the colors – it can be both B&W and full color.
The design should be original and not include any images which require obtaining a copyright license to use. Symbols in common use and not copyrighted are probably ok.
Text for the back cover is not yet available, will be ready by the end of the project. I will need PDF, JPEG, TIFF (all formats both in CMYK and RGB), and the source file. For CMYK, we need files with no color profiles assigned.
I have several options in my mind (But please do not limit yourself by these options - please feel free to suggest your vision):
1) Is Gradient morning clear sky and the star constellation and image at skyrise (like a rising star)
2) solid dark color with image and symbols of the Zodiac sign
75% of my auditory are women

```html
<!DOCTYPE html>
<html lang="en">
<head>
<meta charset="utf-8">
<title>Whole Stargazer Journal &amp; Logbook – Sign One 2022</title>
<link href="https://fonts.googleapis.com/css2?family=Bebas+Neue&family=Montserrat:wght@400;600&display=swap" rel="stylesheet">
<style>
  :root {
    --page-bg: #bdbdbd;
    --cover-bg: #0b0b0c;
    --ink: #f2f2f2;
    --ink-soft: #d6d6d6;
    --silver-light: #ffffff;
    --silver-dark: #8e8e8e;
    --frame: #e8e8e8;
  }
  * { margin: 0; padding: 0; box-sizing: border-box; }
  html, body {
    width: 1200px;
    height: 2192px;
    overflow: hidden;
    background: var(--page-bg);
  }
  .cover {
    position: absolute;
    left: 100px;
    top: 373px;
    width: 1000px;
    height: 1446px;
    background: var(--cover-bg);
    box-shadow: 6px 10px 22px rgba(0,0,0,0.35);
    color: var(--ink);
    text-align: center;
  }
  .cover-frame {
    position: absolute;
    inset: 0;
  }
  .line-title {
    position: absolute;
    left: 0;
    width: 100%;
    display: flex;
    align-items: center;
    justify-content: center;
    gap: 28px;
  }
  .rule {
    width: 92px;
    height: 3px;
    background: linear-gradient(90deg, transparent, var(--ink) 30%, var(--ink) 70%, transparent);
  }
  .kicker {
    top: 118px;
    font-family: "Montserrat", sans-serif;
    font-weight: 600;
    font-size: 50px;
    letter-spacing: 1px;
  }
  .main-title {
    position: absolute;
    top: 200px;
    width: 100%;
    font-family: "Bebas Neue", sans-serif;
    font-size: 116px;
    line-height: 1;
    letter-spacing: 2px;
    background: linear-gradient(180deg, var(--silver-light) 0%, #d9d9d9 45%, var(--silver-dark) 55%, #e6e6e6 100%);
    -webkit-background-clip: text;
    background-clip: text;
    color: transparent;
  }
  .subtitle {
    position: absolute;
    top: 322px;
    width: 100%;
    font-family: "Montserrat", sans-serif;
    font-weight: 600;
    font-size: 46px;
    letter-spacing: 1px;
    color: var(--ink-soft);
  }
  .sign-line {
    position: absolute;
    top: 400px;
    width: 100%;
    font-family: "Bebas Neue", sans-serif;
    font-size: 54px;
    letter-spacing: 1px;
  }
  .year {
    top: 484px;
    font-family: "Montserrat", sans-serif;
    font-weight: 600;
    font-size: 46px;
  }
  .year .rule { width: 150px; }
  .zodiac-wheel {
    position: absolute;
    left: 227px;
    top: 577px;
    width: 480px;
    height: 480px;
    margin-left: 20px;
  }
  .tagline {
    position: absolute;
    top: 1322px;
    left: 200px;
    width: 600px;
    font-family: "Montserrat", sans-serif;
    font-weight: 400;
    font-size: 21.5px;
    line-height: 1.3;
    color: var(--ink-soft);
  }
</style>
</head>
<body>
  <main class="cover">
    <svg class="cover-frame" width="1000" height="1446" viewBox="0 0 1000 1446" aria-hidden="true">
      <polygon points="88,56 912,56 956,100 956,1364 912,1407 88,1407 44,1364 44,100"
               fill="none" stroke="var(--frame)" stroke-width="2.5"/>
    </svg>

    <div class="line-title kicker"><span class="rule"></span><span>WHOLE</span><span class="rule"></span></div>
    <h1 class="main-title">STARGAZER</h1>
    <h2 class="subtitle">JOURNAL &amp; LOGBOOK</h2>
    <p class="sign-line">SIGN ONE (SIGN TWO, SIGN THREE ETC)</p>
    <div class="line-title year"><span class="rule"></span><span>2022</span><span class="rule"></span></div>

    <svg class="zodiac-wheel" viewBox="0 0 480 480" role="img" aria-label="Zodiac wheel with the twelve sign figures around a central sun">
      <defs>
        <radialGradient id="wheelTone" cx="50%" cy="50%" r="50%">
          <stop offset="0%" stop-color="#6a6a6a"/>
          <stop offset="35%" stop-color="#2b2b2b"/>
          <stop offset="100%" stop-color="#1a1a1a"/>
        </radialGradient>
      </defs>
      <circle cx="240" cy="240" r="238" fill="url(#wheelTone)"/>
    </svg>

    <p class="tagline">Shape your days by charting Orbital and Night angles and passages, Idle Drift, Night cycles, Sky almanac, and Reversing bodies.</p>
  </main>
</body>
</html>
```